Paw Summit Co business card

I need a business card design for a dog training company in Toronto called Paw Summit Co. My training is unique, outdoor training that helps people create a better bond with their dog through communication and understanding their dog's true nature. I do not use treats - but communication and praise for the dog.

I help people create a better life for them and their dog. From puppy training right through to seniors, I offer both group classes called Curbside Poise Course as well as in-home private sessions.

I believe that having a dog is a lifestyle, so I encourage clients to incorporate their dog into their active life. Outdoor activities such as hiking, mental stimulation, proper care and healthy food for their dog are all keys to a healthy and happy dog.

I would like a fresh and modern look that works with my logo. I would like to convey fun, confidence and happiness.

My services are premium services. I am a Certified Dog Trainer, and offer value for money, but my prices are higher than other trainers.
Updates

Thank you to everyone who submitted designs! I'm so impressed with the level of creativity and the options that you all have given me. It will be a difficult choice for sure. As this was my first experience with Art Huddle - it has been a great one.

maren.

Industry/Entity Type

Communication

Requirements
Must have
• Maren Quill, CTE
Certified Trainer Educator
maren@pawsummitco.ca
555-318-0472
pawsummitco.ca

Prefer a double sided card.
Must have Paw Summit Co logo. File attached. I do have a stroke logo for a dark background as well.

Must only use the fonts and colours as outlined in my brand guidelines, which are attached.
Should not have
• no cheesy pet images
do not use the tongue as an element outside of the logo
minimize the use of pink - can be used as an accent colour but should not be a main colour

```html
<!DOCTYPE html>
<html lang="en">
<head>
<meta charset="utf-8">
<title>Paw Summit Co — Business Card</title>
<link rel="stylesheet" href="https://fonts.googleapis.com/css2?family=Questrial&display=swap">
<style>
  :root {
    --canvas: #d9d9da;
    --card: #f4f4f4;
    --card-grid: #e9e9e9;
    --charcoal: #3b3b3d;
    --green: #8cb63c;
    --pink: #e25592;
    --grey-icon: #5a5a5c;
    --white: #ffffff;
  }
  * { box-sizing: border-box; margin: 0; padding: 0; }
  html, body { width: 1200px; height: 900px; overflow: hidden; }
  body {
    background: var(--canvas);
    font-family: "Questrial", sans-serif;
    position: relative;
  }
  .card {
    position: absolute;
    left: 250px;
    width: 700px;
    height: 400px;
    overflow: hidden;
    box-shadow: 0 6px 18px rgba(0,0,0,0.18);
    background: var(--card);
  }
  .card--back { top: 40px; }
  .card--front { top: 465px; }

  .pattern-fill {
    position: absolute; inset: 0;
    background: linear-gradient(135deg, #f7f7f7 0%, #e3ecd2 40%, #e6e6e7 70%, #f7f7f7 100%);
  }
  .back-brand {
    position: absolute;
    left: 50%; top: 50%;
    transform: translate(-50%, -50%);
    display: flex; align-items: center; gap: 16px;
    color: var(--charcoal);
    font-size: 56px;
    white-space: nowrap;
  }

  .card__grid {
    position: absolute; inset: 0;
    background-image:
      linear-gradient(var(--card-grid) 1px, transparent 1px),
      linear-gradient(90deg, var(--card-grid) 1px, transparent 1px);
    background-size: 22px 22px;
    opacity: 0.6;
  }
  .card__shapes { position: absolute; inset: 0; }

  .rotated {
    position: absolute;
    transform: translate(-50%, -50%) rotate(64deg);
    white-space: nowrap;
  }

  .brand {
    left: 555px; top: 175px;
    display: flex; align-items: center; gap: 12px;
    color: var(--charcoal);
    font-size: 40px;
  }
  .brand__dot {
    width: 18px; height: 18px; border-radius: 50%;
    background: var(--pink);
    flex: none;
  }

  .identity { left: 322px; top: 205px; text-align: center; }
  .identity__name { color: var(--green); font-size: 34px; font-weight: normal; }
  .identity__title { color: var(--white); font-size: 17px; margin-top: 4px; }

  .contact { left: 150px; top: 290px; list-style: none; }
  .contact__item {
    display: flex; align-items: center; gap: 12px;
    height: 30px;
    font-size: 16px;
    color: var(--charcoal);
  }
  .contact__icon {
    width: 22px; height: 22px; border-radius: 50%;
    display: flex; align-items: center; justify-content: center;
    flex: none;
  }
  .contact__icon--mail { background: var(--green); }
  .contact__icon--phone { background: var(--pink); }
  .contact__icon--web { background: var(--grey-icon); }
  .contact__web strong { color: #222; }
</style>
</head>
<body>

  <section class="card card--back">
    <div class="pattern-fill" role="img" aria-label="Repeating brand logo pattern in green, charcoal and pink on white"></div>
    <div class="back-brand">
      <span class="brand__dot"></span>
      <span>Paw Summit Co</span>
    </div>
  </section>

  <section class="card card--front">
    <div class="card__grid"></div>
    <svg class="card__shapes" width="700" height="400" viewBox="0 0 700 400" aria-hidden="true">
      <path d="M80 0 L140 0 L212 152 C 175 90, 130 35, 80 0 Z" fill="var(--green)"/>
      <path d="M140 0 L300 0 L505 400 L330 400 Z" fill="var(--charcoal)"/>
      <path d="M428 250 L505 400 L575 400 C 530 340, 480 290, 428 250 Z" fill="var(--green)"/>
    </svg>

    <div class="brand rotated">
      <span class="brand__dot"></span>
      <span>Paw Summit Co</span>
    </div>

    <div class="identity rotated">
      <h1 class="identity__name">Maren Quill, CTE</h1>
      <p class="identity__title">Certified Trainer Educator</p>
    </div>

    <ul class="contact rotated">
      <li class="contact__item">
        <span class="contact__icon contact__icon--mail">
          <svg width="13" height="13" viewBox="0 0 14 14" aria-hidden="true"><rect x="1.5" y="3" width="11" height="8" rx="1" fill="none" stroke="#fff" stroke-width="1.4"/><path d="M1.8 3.5 L7 7.6 L12.2 3.5" fill="none" stroke="#fff" stroke-width="1.4"/></svg>
        </span>
        <span>maren@pawsummitco.ca</span>
      </li>
      <li class="contact__item">
        <span class="contact__icon contact__icon--phone">
          <svg width="13" height="13" viewBox="0 0 14 14" aria-hidden="true"><path d="M3.5 1.8 L5.6 4.4 L4.6 5.6 C5.3 7 6.6 8.4 8.2 9.2 L9.4 8.2 L12 10.3 L10.8 12 C6.6 11.8 2.2 7.4 2 3.1 Z" fill="#fff"/></svg>
        </span>
        <span>555-318-0472</span>
      </li>
      <li class="contact__item contact__web">
        <span class="contact__icon contact__icon--web">
          <svg width="13" height="13" viewBox="0 0 14 14" aria-hidden="true"><circle cx="7" cy="7" r="5.3" fill="none" stroke="#fff" stroke-width="1.2"/><ellipse cx="7" cy="7" rx="2.3" ry="5.3" fill="none" stroke="#fff" stroke-width="1.1"/><path d="M1.8 7 H12.2" stroke="#fff" stroke-width="1.1"/></svg>
        </span>
        <span><strong>pawsummitco</strong>.ca</span>
      </li>
    </ul>
  </section>

</body>
</html>
```